Design a modern, classy & professional business card for an online real estate agency, specializing in medium-luxury properties in Thailand and later in Singapore and UK.

Possible design ideas so far: (not essential)

- curved corner(s) to the card, white on front & turquoise on back or visa versa.

- front of card - clear and simple, company name in metallic grey/monochrome, logo graphic & company name on front in spot UV or embossed/debossed effect.

- back of card - large, close-cropped, 'ghost' patterns of the C-shaped curves of logo, or company name repeated on back of card in spot UV.

Target Market(s)

- young to middle-aged professionals mainly (but ideally should design should suit all)

- UK, US,EU,AUS & ASIAN mainly (but ideally should design should suit all countries)

Industry/Entity Type

Real Estate

Requirements
Must have
• THEME:
- Luxurious & Modern
- Clean & striking
- Unique & creative

INFO:
- Logo & company name on front
- Contact details on back:

Tobias Lindqvist
Managing Director

www.velmoraestates.example
www.velmoraestates-uk.example

Tel: 083-274-6190
email: tobias@velmoraestates.example

(contact details can be displayed in any order as suites design.)

Nice to have
• - curved corner(s) to the card, white on front & turquoise on back or visa versa.

Should not have
• - No generic images of properties, palm trees/coconut trees etc.

- No other other bold colors, except for main turquoise, grey, metallic white & black theme.

- No obvious business card templates

```html
<!DOCTYPE html>
<html lang="en">
<head>
<meta charset="utf-8">
<title>Velmora Estates – Business Card</title>
<link rel="stylesheet" href="https://fonts.googleapis.com/css2?family=Cormorant+Garamond:wght@500&family=Roboto+Condensed:wght@400;700&display=swap">
<style>
  :root {
    --turquoise: #5bbcb8;
    --turquoise-deep: #3fa19d;
    --grey: #77797c;
    --ink: #1e1f21;
    --card: #ffffff;
    --ghost: #f1f2f3;
    --stage: #e6e7e8;
  }
  * { margin: 0; padding: 0; box-sizing: border-box; }
  html, body { width: 1200px; height: 913px; overflow: hidden; }
  body {
    background: var(--stage);
    font-family: "Roboto Condensed", Arial, sans-serif;
    position: relative;
  }
  .card {
    position: absolute;
    width: 520px;
    height: 300px;
    border-radius: 22px;
    background: var(--card);
    overflow: hidden;
    box-shadow: 0 6px 18px rgba(0,0,0,.12);
  }
  .card--front { left: 60px; top: 306px; }
  .card--back { left: 620px; top: 306px; }

  .ghost-pattern {
    position: absolute;
    inset: 0;
    background: radial-gradient(ellipse at 50% 50%, var(--ghost) 0%, #f7f8f8 60%, var(--card) 100%);
  }

  .brand {
    position: absolute;
    display: flex;
    align-items: center;
    gap: 14px;
  }
  .brand__square {
    background: var(--turquoise);
    flex: none;
  }
  .brand__name {
    font-family: "Cormorant Garamond", Georgia, serif;
    font-weight: 500;
    color: var(--grey);
    white-space: nowrap;
    line-height: 1;
  }
  .card--front .brand { left: 50%; top: 50%; transform: translate(-50%, -50%); }
  .card--front .brand__square { width: 76px; height: 76px; }
  .card--front .brand__name { font-size: 46px; }

  .card--back .brand { left: 34px; top: 40px; gap: 12px; }
  .card--back .brand__square { width: 54px; height: 54px; }
  .card--back .brand__name { font-size: 32px; }

  .person {
    position: absolute;
    right: 30px;
    top: 44px;
    text-align: right;
  }
  .person__name { color: var(--turquoise); font-weight: 700; font-size: 17px; letter-spacing: .3px; }
  .person__role { color: var(--ink); font-size: 13px; margin-top: 3px; }

  .contacts {
    position: absolute;
    left: 40px;
    top: 130px;
    list-style: none;
  }
  .contacts li {
    display: flex;
    align-items: center;
    gap: 10px;
    font-size: 14px;
    font-weight: 700;
    color: var(--ink);
    height: 24px;
  }
  .contacts svg { width: 14px; height: 14px; flex: none; fill: var(--turquoise-deep); }

  .edge-band {
    position: absolute;
    left: 0; right: 0; bottom: 0;
    height: 16px;
    background: linear-gradient(90deg, var(--turquoise-deep), var(--turquoise));
  }
</style>
</head>
<body>

<section class="card card--front" aria-label="Card front">
  <div class="ghost-pattern" role="img" aria-label="Faint spot-UV pattern of interlocking curves"></div>
  <div class="brand">
    <span class="brand__square"></span>
    <span class="brand__name">Velmora Estates</span>
  </div>
</section>

<section class="card card--back" aria-label="Card back">
  <div class="ghost-pattern" role="img" aria-label="Faint spot-UV pattern of interlocking curves"></div>
  <div class="brand">
    <span class="brand__square"></span>
    <span class="brand__name">Velmora Estates</span>
  </div>

  <div class="person">
    <p class="person__name">Tobias Lindqvist</p>
    <p class="person__role">Managing Director</p>
  </div>

  <ul class="contacts">
    <li>
      <svg viewBox="0 0 16 16" aria-hidden="true"><path d="M3 1h3l1.5 4-2 1.3a9 9 0 0 0 4.2 4.2L11 8.5l4 1.5v3a2 2 0 0 1-2 2A12 12 0 0 1 1 3a2 2 0 0 1 2-2z"/></svg>
      083-274-6190
    </li>
    <li>
      <svg viewBox="0 0 16 16" aria-hidden="true"><path d="M1 3h14v10H1z M1.8 3.6 8 8.6l6.2-5H1.8z" fill-rule="evenodd"/></svg>
      tobias@velmoraestates.example
    </li>
    <li>
      <svg viewBox="0 0 16 16" aria-hidden="true"><circle cx="8" cy="8" r="7"/><path d="M1 8h14M8 1c-3 3.5-3 10.5 0 14M8 1c3 3.5 3 10.5 0 14" stroke="#fff" stroke-width="1" fill="none"/></svg>
      www.velmoraestates.example
    </li>
    <li>
      <svg viewBox="0 0 16 16" aria-hidden="true"></svg>
      www.velmoraestates-uk.example
    </li>
  </ul>

  <div class="edge-band"></div>
</section>

</body>
</html>
```